Bluewake Harbor Skipper Services LLC

I'd like business cards with a logo and words to describe my services and qualifications. I want to emphasize the wide variety of services offered and my professional qualifications. Words to include "Bluewake Harbor Skipper Services LLC", "Motor and Sailing Vessel Delivery, Charter, Surveys, Towing and Instruction". Qualifications I would like to include are "Captain Dale Murrow, USCG Master Mariner, 200 ton, Ocean". Include address, phone and email: "48215 Willowmere Lane, Fairfax Station, VA 22871, (C) 703-555-0187, BluewakeHarborSkipper@mailbay-example.com"

Target Market(s)

I am targeting recreational boaters and commercial customers that need people to operate their boats for charter or delivery to another location.

Industry/Entity Type

boat selling/buying, boat charter, boat recreation

Logo Text

"Motor and Sailing Vessel Delivery, Charters, Surveys, Towing and Instruction"

Requirements
Must have
• A professional and nautical look.
Nice to have
• May be nice to have a muted chart as the background design
Should not have
• colors or design that obscure the message of offering a wide range of professional boat captain services

```html
<!DOCTYPE html>
<html lang="en">
<head>
<meta charset="utf-8">
<title>Bluewake Harbor Skipper Services LLC – Business Card</title>
<link rel="stylesheet" href="https://fonts.googleapis.com/css2?family=Montserrat:wght@400;500;700;800&display=swap">
<style>
  :root {
    --backdrop: #2b3a64;
    --card: #e2e7f0;
    --land: #fbfcfe;
    --land-soft: rgba(251, 252, 254, 0.85);
    --grid: rgba(160, 172, 196, 0.22);
    --ink: #25335d;
    --ocean-label: #a4acbc;
    --accent: #3b9ce9;
  }
  * { margin: 0; padding: 0; box-sizing: border-box; }
  html, body {
    width: 1200px;
    height: 900px;
    overflow: hidden;
    background: var(--backdrop);
    font-family: "Montserrat", Arial, sans-serif;
    color: var(--ink);
  }
  .stage {
    position: relative;
    width: 1200px;
    height: 900px;
  }
  .card {
    position: absolute;
    left: 130px;
    top: 168px;
    width: 940px;
    height: 537px;
    background: var(--card);
    box-shadow: 0 4px 14px rgba(0, 0, 0, 0.25);
    overflow: hidden;
  }
  .card__grid {
    position: absolute;
    inset: 0;
    background:
      repeating-linear-gradient(0deg, var(--grid) 0 1px, transparent 1px 24px),
      repeating-linear-gradient(90deg, var(--grid) 0 1px, transparent 1px 24px);
  }
  .card__chart {
    position: absolute;
    inset: 0;
    background:
      radial-gradient(ellipse 13% 17% at 25% 22%, var(--land-soft) 0%, transparent 100%),
      radial-gradient(ellipse 8% 20% at 26% 70%, var(--land-soft) 0%, transparent 100%),
      radial-gradient(ellipse 12% 24% at 50% 55%, var(--land-soft) 0%, transparent 100%),
      radial-gradient(ellipse 30% 20% at 66% 22%, var(--land-soft) 0%, transparent 100%),
      radial-gradient(ellipse 9% 10% at 86% 75%, var(--land-soft) 0%, transparent 100%),
      radial-gradient(ellipse 60% 55% at 52% 45%, rgba(245, 247, 251, 0.6) 0%, transparent 100%);
  }
  .ocean-label {
    position: absolute;
    font-size: 13px;
    line-height: 16px;
    font-weight: 500;
    color: var(--ocean-label);
    text-align: center;
    text-transform: uppercase;
  }
  .ocean-label--arctic { left: 515px; top: 10px; width: 60px; }
  .ocean-label--atlantic { left: 268px; top: 190px; width: 100px; }
  .ocean-label--pacific-west { left: 30px; top: 294px; width: 80px; }
  .ocean-label--pacific-east { left: 850px; top: 214px; width: 80px; }

  .credentials {
    position: absolute;
    left: 39px;
    top: 28px;
  }
  .credentials__name {
    font-size: 22px;
    font-weight: 700;
    line-height: 27px;
  }
  .credentials__line {
    font-size: 17px;
    font-weight: 400;
    line-height: 21px;
    padding-left: 6px;
  }

  .brand {
    position: absolute;
    left: 490px;
    top: 115px;
    width: 380px;
    text-align: center;
  }
  .brand__mark {
    display: block;
    width: 72px;
    height: 72px;
    margin: 0 auto 14px;
    border-radius: 50%;
    background: var(--accent);
  }
  .brand__name {
    font-size: 31px;
    font-weight: 800;
    line-height: 36px;
    color: var(--ink);
  }

  .services {
    position: absolute;
    left: 470px;
    top: 310px;
    width: 420px;
    text-align: center;
    font-size: 17px;
    font-weight: 400;
    line-height: 21px;
  }

  .contact {
    position: absolute;
    left: 30px;
    top: 407px;
    font-size: 19px;
    line-height: 23px;
    font-style: normal;
  }
  .contact__email { padding-left: 5px; }
</style>
</head>
<body>
<main class="stage">
  <section class="card">
    <div class="card__grid"></div>
    <div class="card__chart" role="img" aria-label="Muted world chart with white continents on a light grid"></div>
    <span class="ocean-label ocean-label--arctic">Artic<br>Ocean</span>
    <span class="ocean-label ocean-label--atlantic">Atlantic<br>Ocean</span>
    <span class="ocean-label ocean-label--pacific-west">Pacific<br>Ocean</span>
    <span class="ocean-label ocean-label--pacific-east">Pacific<br>Ocean</span>

    <div class="credentials">
      <p class="credentials__name">Captain Dale Murrow</p>
      <p class="credentials__line">USCG Master Mariner</p>
      <p class="credentials__line">200 ton, Ocean</p>
    </div>

    <div class="brand">
      <span class="brand__mark"></span>
      <p class="brand__name">Bluewake Harbor<br>Skipper Services LLC</p>
    </div>

    <p class="services">Motor and Sailing Vessel Delivery,<br>Charter, Surveys, Towing and<br>Instruction</p>

    <address class="contact">
      <p>48215 Willowmere Lane</p>
      <p>Fairfax Station, VA 22871</p>
      <p>(C) 703-555-0187</p>
      <p class="contact__email">BluewakeHarborSkipper@mailbay-example.com</p>
    </address>
  </section>
</main>
</body>
</html>
```